DEAN COLLOPY PROPERTY SERVICES

I want a business card that is clean and simple.
'Dean Collopy Property Services' is the title.
Somewhere on the card needs to be 'Carpentry, Tiling, painting and garden services'

On the back of card
PH 087 394 1526
email: deancollopypropertyservices@fernmail.net

I have attached a picture of my other business. I would like the font and design to be similar to the bathroom business.

Many thanks.

```html
<!DOCTYPE html>
<html lang="en">
<head>
<meta charset="utf-8">
<title>Dean Collopy Property Services – Business Card</title>
<link href="https://fonts.googleapis.com/css2?family=Montserrat:wght@400;500;600&family=Arimo:wght@400&display=swap" rel="stylesheet">
<style>
  :root {
    --backdrop: #0b0b0c;
    --card: #2a2a2c;
    --card-edge: #dcdcdc;
    --ink: #ffffff;
    --ink-soft: #d9d9d9;
    --rule: #6a6a6c;
    --emboss: #4a4a4d;
    --emboss-light: #5c5c60;
  }
  * { margin: 0; padding: 0; box-sizing: border-box; }
  html, body {
    width: 1200px; height: 820px; overflow: hidden;
    background: radial-gradient(ellipse at 50% 35%, #1c1c1e 0%, var(--backdrop) 75%);
  }
  .stage { position: relative; width: 1200px; height: 820px; }
  .card {
    position: absolute; width: 540px; height: 320px;
    background: var(--card);
    border-radius: 3px;
    box-shadow: 0 0 0 1px var(--card-edge), 0 18px 40px rgba(0,0,0,.7);
    overflow: hidden;
  }
  .card--front { left: 70px; top: 440px; }
  .card--back { left: 600px; top: 90px; }

  .wordmark { font-family: "Montserrat", sans-serif; font-weight: 500; line-height: 1; }
  .wordmark__name { display: block; letter-spacing: -0.5px; }
  .wordmark__sub { display: block; letter-spacing: 4px; text-transform: uppercase; }

  .card--front .wordmark {
    position: absolute; right: 44px; top: 56px; text-align: right; color: var(--ink);
  }
  .card--front .wordmark__name { font-size: 40px; }
  .card--front .wordmark__sub { font-size: 13px; margin-top: 6px; }

  .divider-top {
    position: absolute; left: 250px; right: 30px; top: 148px;
    height: 1px; background: var(--rule);
  }
  .holder { position: absolute; left: 36px; top: 196px; }
  .holder__name {
    font-family: "Montserrat", sans-serif; font-weight: 600; font-size: 20px;
    color: var(--ink); letter-spacing: .5px;
  }
  .holder__role {
    font-family: "Arimo", sans-serif; font-size: 14px; color: var(--ink-soft);
    margin-top: 3px; display: flex; align-items: center; gap: 12px;
  }
  .holder__role::after { content: ""; width: 300px; height: 1px; background: var(--rule); }
  .contact { position: absolute; left: 36px; top: 262px; list-style: none; }
  .contact__item {
    font-family: "Arimo", sans-serif; font-size: 15px; color: var(--ink);
    display: flex; align-items: center; gap: 8px; height: 22px;
  }
  .contact__icon { width: 15px; height: 15px; fill: none; stroke: var(--ink); stroke-width: 1.6; }

  .card--back .wordmark {
    position: absolute; left: 0; right: 0; top: 92px; text-align: center;
    color: var(--emboss);
    text-shadow: -1px -1px 0 var(--emboss-light), 1px 1px 1px #1b1b1c;
  }
  .card--back .wordmark__name { font-size: 48px; }
  .card--back .wordmark__sub { font-size: 15px; margin-top: 8px; letter-spacing: 5px; }
  .services {
    position: absolute; left: 0; right: 0; top: 232px; text-align: center;
    font-family: "Arimo", sans-serif; font-size: 15px; color: var(--ink-soft);
    display: flex; justify-content: center; align-items: center; gap: 10px;
  }
  .services__dot { width: 6px; height: 6px; border-radius: 50%; background: var(--ink-soft); }
</style>
</head>
<body>
<main class="stage">
  <section class="card card--back" aria-label="Card back">
    <div class="wordmark">
      <span class="wordmark__name">Dean Collopy</span>
      <span class="wordmark__sub">Property Services</span>
    </div>
    <p class="services">
      <span>Carpentry</span><span class="services__dot"></span>
      <span>Tiling</span><span class="services__dot"></span>
      <span>Painting</span><span class="services__dot"></span>
      <span>Garden Services</span>
    </p>
  </section>

  <section class="card card--front" aria-label="Card front">
    <div class="wordmark">
      <span class="wordmark__name">Dean Collopy</span>
      <span class="wordmark__sub">Property Services</span>
    </div>
    <div class="divider-top"></div>
    <div class="holder">
      <p class="holder__name">CIARAN DOYLE</p>
      <p class="holder__role">Managing Director</p>
    </div>
    <ul class="contact">
      <li class="contact__item">
        <svg class="contact__icon" viewBox="0 0 16 16" aria-hidden="true">
          <path d="M3 1.5h3l1.2 3.2-1.8 1.2a8 8 0 0 0 4.7 4.7l1.2-1.8 3.2 1.2v3a1.5 1.5 0 0 1-1.6 1.5A13 13 0 0 1 1.5 3.1 1.5 1.5 0 0 1 3 1.5z"/>
        </svg>
        087 394 1526
      </li>
      <li class="contact__item">
        <svg class="contact__icon" viewBox="0 0 16 16" aria-hidden="true">
          <rect x="1" y="3" width="14" height="10" rx="1"/>
          <path d="M1.5 3.5 8 9l6.5-5.5"/>
        </svg>
        deancollopypropertyservices@fernmail.net
      </li>
    </ul>
  </section>
</main>
</body>
</html>
```